Medical Billing - Professional Marketing Flier

We are needing help designing a clean and professional looking easy to read marketing flier for a medical billing practice. The text needs to be large enough to print. We are looking for a 5.5 x 8.5 design that we can edit the text as needed. I have included our logo and what we initially want it to say. Please keep in mind, we also want our logo and contact details on the flier. Let me know if you have any questions.

```html
<!DOCTYPE html>
<html lang="en">
<head>
<meta charset="utf-8">
<title>Vela Medical Billing – Flier</title>
<link href="https://fonts.googleapis.com/css2?family=Cinzel:wght@400;500&family=Poppins:wght@300;400;500;600&display=swap" rel="stylesheet">
<style>
  :root{
    --purple:#6a5cb6;
    --violet:#8e5fc0;
    --pink:#d15ba8;
    --ink:#3b3b40;
    --ink-strong:#2d2d33;
    --night:#121015;
    --night-soft:#1e1b22;
    --paper:#ffffff;
    --backdrop:#777777;
    --photo-light:#f4f4f7;
    --photo-mid:#e3e2e8;
  }
  *{box-sizing:border-box;margin:0;padding:0}
  html,body{width:1200px;height:840px;overflow:hidden;background:var(--backdrop)}
  .flier{position:absolute;left:20px;top:44px;width:1160px;height:751px;background:var(--paper);overflow:hidden;font-family:'Poppins',sans-serif;color:var(--ink)}
  .top-band{position:absolute;left:0;top:0;width:100%;height:16px;background:linear-gradient(90deg,var(--purple),var(--pink))}
  .hero-photo{position:absolute;left:360px;top:16px;width:800px;height:446px;background:radial-gradient(ellipse at 55% 50%,var(--photo-mid),var(--photo-light) 60%,var(--paper) 100%)}
  .hero-photo::before{content:"";position:absolute;inset:0;background:linear-gradient(90deg,var(--paper),rgba(255,255,255,0) 30%)}
  .brand{position:absolute;left:80px;top:128px;width:270px;text-align:center;font-family:'Cinzel',serif;font-weight:500;color:var(--purple)}
  .brand-name{font-size:50px;line-height:1;letter-spacing:2px;display:block}
  .brand-tag{font-size:15px;letter-spacing:4px;display:block;margin-top:8px}
  .divider-band{position:absolute;left:0;top:460px;width:100%;height:8px;background:linear-gradient(90deg,var(--pink),var(--purple))}
  .night{position:absolute;left:0;top:468px;width:100%;height:283px;background:linear-gradient(90deg,var(--night),var(--night-soft))}
  .service{position:absolute;top:264px;width:345px;height:312px;background:var(--paper);border:2px solid var(--violet);border-radius:14px;padding:26px 18px 0 26px}
  .service:nth-of-type(1){border-color:var(--pink)}
  .service-1{left:60px}.service-2{left:418px}.service-3{left:776px}
  .service-icon{position:absolute;left:18px;top:-34px;width:60px;height:50px;background:var(--paper);display:flex;justify-content:center;align-items:flex-start}
  .service-title{font-family:'Cinzel',serif;font-weight:500;font-size:25px;color:var(--purple);letter-spacing:.5px;line-height:1.1;margin-bottom:10px}
  .service-question{font-weight:600;font-size:13px;line-height:17.5px;color:var(--ink-strong);margin-bottom:7px}
  .service-body{font-weight:400;font-size:13px;line-height:17.3px;color:var(--ink)}
  .contact{position:absolute;left:87px;top:594px;width:650px;color:#e9e9ee}
  .contact-title{font-family:'Cinzel',serif;font-weight:400;font-size:27px;letter-spacing:1px;color:#fff;margin-bottom:6px}
  .contact-text{font-size:13px;font-weight:300;line-height:17.5px}
  .contact-text strong{color:var(--pink);font-weight:500}
  .call-pill{position:absolute;left:810px;top:620px;width:301px;height:36px;background:var(--pink);border-radius:6px;color:#fff;font-size:20px;display:flex;align-items:center;justify-content:center;gap:6px}
  .call-pill b{font-weight:600;letter-spacing:.5px}
  .contact-line{position:absolute;left:812px;font-size:16.5px;font-weight:300;color:#f0f0f4;display:flex;align-items:center;gap:8px}
  .contact-email{top:646px}.contact-address{top:671px}
</style>
</head>
<body>
<main class="flier">
  <div class="top-band"></div>
  <div class="hero-photo" role="img" aria-label="Photo of a white desk with a stethoscope, paperwork and a keyboard"></div>

  <div class="brand">
    <span class="brand-name">VELA</span>
    <span class="brand-tag">MEDICAL BILLING</span>
  </div>

  <div class="divider-band"></div>
  <div class="night"></div>

  <section class="service service-1">
    <div class="service-icon">
      <svg width="44" height="46" viewBox="0 0 44 46" fill="none" stroke="#7a5cc0" stroke-width="1.6"><rect x="8" y="2" width="26" height="40" rx="2"/><circle cx="21" cy="12" r="6"/><path d="M21 9v6M18 12h6M12 24h18M12 29h14M12 34h10"/><circle cx="34" cy="32" r="6" stroke="#d15ba8"/><path d="M34 29v6" stroke="#d15ba8"/></svg>
    </div>
    <h2 class="service-title">MEDICAL BILLING</h2>
    <p class="service-question">Would you prefer to spend time focusing on your clients and running your practice rather than trying to stay up to speed with the constantly changing medical billing rules and regulations?</p>
    <p class="service-body">Let us help you by managing your medical billing and dealing with the insurance companies on your behalf! We work with you to tailor the entire medical billing process to suit your practices needs while making it as smooth and painless as possible.</p>
  </section>

  <section class="service service-2">
    <div class="service-icon">
      <svg width="50" height="46" viewBox="0 0 50 46" fill="none" stroke="#7a5cc0" stroke-width="1.6"><rect x="14" y="8" width="30" height="16" rx="2"/><circle cx="29" cy="16" r="4" stroke="#d15ba8"/><path d="M4 4h10l6 6M4 30h8c6 0 10 4 18 4h10v8H28c-8 0-12-4-24-4"/></svg>
    </div>
    <h2 class="service-title">AGING</h2>
    <p class="service-question">Are you leaving money on the table? Are you able to do the follow-through needed to keep your aging in check and more money flowing into your practice?</p>
    <p class="service-body">Are you uncertain about how to get insurance to pay on claims that should be covered but for some reason they decided not to? We can clean up your aging, reduce the amount of time it takes for claims to pay out, and we can keep your aging to a minimum.</p>
  </section>

  <section class="service service-3">
    <div class="service-icon">
      <svg width="46" height="46" viewBox="0 0 46 46" fill="none" stroke="#7a5cc0" stroke-width="1.6"><path d="M6 4h24l6 6v32H6z"/><path d="M11 14h16M11 20h18M11 26h12M11 32h10"/><circle cx="34" cy="30" r="6" stroke="#d15ba8"/><path d="M31 35l-2 8 5-3 5 3-2-8" stroke="#d15ba8"/></svg>
    </div>
    <h2 class="service-title">CREDENTIALING</h2>
    <p class="service-question">Are you wanting to get contracted with insurance companies but aren’t sure how to go about it?</p>
    <p class="service-question">Are you wanting to expand your client base by having the option to bill insurance?</p>
    <p class="service-body">Let us take the confusion out of what can seem like a daunting task! We can get you and your practitioners contracted with the insurance companies of your choice and help you navigate through the process every step of the way!</p>
  </section>

  <section class="contact">
    <h2 class="contact-title">CONTACT US</h2>
    <p class="contact-text">If any of these processes are something you would like our help with or to <strong>consult with us on, please email us or give us a call!</strong> We specialize in billing and contracting for Nutritionists and Dietitians. We would love to help you expand your business and take the pain and frustration out of billing so you can focus on your clients</p>
  </section>

  <div class="call-pill">
    <svg width="20" height="16" viewBox="0 0 20 16" fill="#fff"><path d="M1 5c0-3 4-4 9-4s9 1 9 4v2h-5V5H6v2H1z"/><path d="M4 8h12l2 7H2z"/></svg>
    <span>Call Us <b>425-555-0173</b></span>
  </div>
  <div class="contact-line contact-email">
    <svg width="17" height="12" viewBox="0 0 17 12" fill="none" stroke="#fff" stroke-width="1.2"><rect x=".6" y=".6" width="15.8" height="10.8"/><path d="M.6.6l7.9 6 7.9-6"/></svg>
    <span>admin@velamedicalbilling.com</span>
  </div>
  <div class="contact-line contact-address">
    <svg width="15" height="15" viewBox="0 0 15 15" fill="#fff"><path d="M14 1L1 7l6 1 1 6z"/></svg>
    <span>PO Box 418 Cedar Falls, WA 98099</span>
  </div>
</main>
</body>
</html>
```